Business and Success Coaching Business Card

Need a business card for my coaching business. I coach small businesses, career professionals and, individuals wanting to unlock their human potential and achieve excellence. At the heart of our methodology is the Shaping Purposeful Action Routines Knowingly (SPARK) approach to formulate empowerment, create principles for success and setting achievable outcomes. I would like something that incorporates our new logo, something clean and sharp with a solid darker, but complementary background, color on the card front. The back should be white where there will be room for three questions

Target Market(s)

People looking to advance and improve themselves through a success coach

Industry/Entity Type

Life Coaching

Contact Information for Business Card

Contact information on card.
Business name on front of card
Questions on back

Font styles to use
Other font styles liked:
• Century Gothic or other Serif style fonts that look similar to Century Gothic

Colors

Designer to choose colors to be used in the design.

Requirements
Must have
• Logo on front of card
• Business name - The Steady Forge
• Contact name - Ted Harlow
• Address - Box 4619, Littleton, CO 80127-4619
• Phone number - 303-555-0147
• Email address - harlow.ted@thesteadyforge.example
• Certifications - CSC, CCHt, PTT, PNLP
• Back of card
• Three questions on the back of the card:
• If you were at your best, what would you do right now?
• What is the decision you have been avoiding?
• What's one action you could take in the next 10 minutes?
Nice to have
• I would like to see a solid color on the front of the card that compliments the logo.
• Back should be white, or could be contrasting, but need to have the three questions.

```html
<!DOCTYPE html>
<html lang="en">
<head>
<meta charset="utf-8">
<title>The Steady Forge – Business Card</title>
<link rel="stylesheet" href="https://fonts.googleapis.com/css2?family=Open+Sans:wght@400;600;700&display=swap">
<style>
  :root {
    --page-bg: #e6e6e6;
    --paper: #f3f4f6;
    --navy: #1f3368;
    --navy-top: #2c4577;
    --band-blue: #4a83c6;
    --mark-blue: #4a84c8;
    --tagline-light: #a9c1e2;
    --white: #ffffff;
    --soft-white: #e4e9f2;
  }
  * { box-sizing: border-box; margin: 0; padding: 0; }
  html, body { width: 1200px; height: 1200px; overflow: hidden; }
  body {
    background: var(--page-bg);
    font-family: "Open Sans", Arial, sans-serif;
    position: relative;
  }
  .card {
    position: absolute;
    left: 264px;
    width: 686px;
    height: 392px;
    border-radius: 21px;
    overflow: hidden;
  }
  .card-front { top: 165px; background: var(--paper); }
  .card-back {
    top: 653px;
    background: linear-gradient(180deg, var(--navy-top) 0%, var(--navy) 100%);
  }
  .brand-dot {
    position: absolute;
    left: 50%;
    width: 96px;
    height: 96px;
    margin-left: -48px;
    border-radius: 50%;
  }
  .card-front .brand-dot { top: 52px; background: var(--mark-blue); }
  .card-back .brand-dot { top: 82px; background: var(--soft-white); }
  .brand-name {
    position: absolute;
    left: 0; right: 0;
    text-align: center;
    font-weight: 600;
    font-size: 34px;
    letter-spacing: -0.3px;
    line-height: 1;
  }
  .card-front .brand-name { top: 183px; color: var(--navy); }
  .card-back .brand-name { top: 217px; color: var(--white); }
  .tagline {
    position: absolute;
    left: 0; right: 0;
    text-align: center;
    font-size: 19px;
    line-height: 1;
  }
  .card-front .tagline { top: 216px; color: var(--tagline-light); }
  .card-back .tagline { top: 251px; color: var(--soft-white); }

  .contact-band {
    position: absolute;
    left: 0; right: 0; bottom: 0;
    height: 121px;
    background: var(--band-blue);
    border-top: 6px solid var(--navy);
  }
  .person {
    position: absolute;
    right: 406px;
    top: 34px;
    text-align: right;
    color: var(--white);
  }
  .person-name { font-size: 28px; font-weight: 600; line-height: 1; letter-spacing: 0.2px; }
  .person-creds { font-size: 13px; margin-top: 6px; }
  .divider {
    position: absolute;
    left: 302px;
    top: 34px;
    width: 2px;
    height: 54px;
    background: var(--white);
  }
  .contact-list {
    position: absolute;
    left: 322px;
    top: 31px;
    list-style: none;
    color: var(--white);
    font-size: 14px;
    line-height: 19px;
  }
  .contact-list li { display: flex; align-items: center; gap: 8px; }
  .contact-list svg { width: 10px; height: 10px; fill: var(--white); flex: none; }

  .question-list {
    position: absolute;
    left: 0; right: 0;
    top: 393px;
    top: 302px;
    list-style: none;
    text-align: center;
    color: var(--soft-white);
    font-size: 12.5px;
    font-weight: 600;
    line-height: 18px;
  }
  .question-list li::before {
    content: "";
    display: inline-block;
    width: 6px; height: 6px;
    border-radius: 50%;
    background: var(--band-blue);
    margin-right: 9px;
    vertical-align: middle;
  }
</style>
</head>
<body>
  <section class="card card-front">
    <div class="brand-dot"></div>
    <h1 class="brand-name">The Steady Forge</h1>
    <p class="tagline">Jump-start your next phase</p>
    <div class="contact-band">
      <div class="person">
        <div class="person-name">TED HARLOW</div>
        <div class="person-creds">CSC, CCHt, PTT, PNLP</div>
      </div>
      <div class="divider"></div>
      <ul class="contact-list">
        <li><svg viewBox="0 0 10 10"><path d="M2 0.5 L3.6 2.6 L2.7 3.6 Q3.8 5.9 6.3 7.2 L7.3 6.3 L9.5 7.9 L8.4 9.5 Q3.5 9 0.5 2 Z"/></svg>303-555-0147</li>
        <li><svg viewBox="0 0 10 10"><path d="M0.5 2 H9.5 V8 H0.5 Z M1.2 2.6 L5 5.4 L8.8 2.6 Z" fill-rule="evenodd"/></svg>harlow.ted@thesteadyforge.example</li>
        <li><svg viewBox="0 0 10 10"><path d="M5 0.3 A3.4 3.4 0 0 1 8.4 3.7 Q8.4 5.8 5 9.7 Q1.6 5.8 1.6 3.7 A3.4 3.4 0 0 1 5 0.3 Z M5 2.4 A1.3 1.3 0 1 0 5 5 A1.3 1.3 0 1 0 5 2.4 Z" fill-rule="evenodd"/></svg>Box 4619, Littleton, CO 80127-4619</li>
      </ul>
    </div>
  </section>

  <section class="card card-back">
    <div class="brand-dot"></div>
    <h2 class="brand-name">The Steady Forge</h2>
    <p class="tagline">Jump-start your next phase</p>
    <ul class="question-list">
      <li>If you were at your best, what would you do right now?</li>
      <li>What is the decision you have been avoiding?</li>
      <li>What's one action you could take in the next 10 minutes?</li>
    </ul>
  </section>
</body>
</html>
```